Business Card Design For Marketing Agnecy LWP

Need business card design for marketing agency.

Dorian Pellow
President, CEO
1-555-302-4196
dorian@brightlanepromotions.example
www.BrightlanePromotions.example

Back Side:
Boost Sales Using Rewards, Incentives & Giveaways
Get A Free Sample Package

Target Market(s)

B2B

Industry/Entity Type

Marketing

Contact Information for Business Card

Dorian Pellow
President, CEO
1-555-302-4196

Back Side:
Get A Free Sample Package

Please note that my current url is OLD DESIGN. I am working on new design and want the business card to match color themes at least on new site. Here is the demo link for new site so you can see the colors I use, etc.

http://pixelquarrydemo.example/dh/dorian/lwp_final/index.html

Requirements
Must have
• Please note that my current url is OLD DESIGN. I am working on new design and want the business card to match color themes at least on new site. Here is the demo link for new site so you can see the colors I use, etc.

Nice to have

Should not have

```html
<!DOCTYPE html>
<html lang="en">
<head>
<meta charset="utf-8">
<title>LWP Business Card</title>
<link rel="stylesheet" href="https://fonts.googleapis.com/css2?family=Open+Sans:wght@400;600;700;800&display=swap">
<style>
  :root {
    --brand-blue: #1474c0;
    --brand-blue-deep: #0c5aa0;
    --navy: #0a3f7e;
    --navy-dark: #072e60;
    --ink: #3a3a3a;
    --paper: #ffffff;
    --paper-shade: #eeeeee;
    --backdrop: #c9c9c9;
    --white: #ffffff;
  }
  html, body {
    margin: 0;
    padding: 0;
    width: 1200px;
    height: 900px;
    overflow: hidden;
    background: var(--backdrop);
    font-family: "Open Sans", Arial, sans-serif;
  }
  .canvas {
    position: relative;
    width: 1200px;
    height: 900px;
  }
  .card {
    position: absolute;
    width: 525px;
    height: 300px;
    overflow: hidden;
    box-shadow: 0 6px 18px rgba(0,0,0,0.25);
  }

  /* Back side */
  .card-back {
    left: 70px;
    top: 150px;
    background: linear-gradient(135deg, var(--navy-dark) 0%, var(--navy) 45%, var(--brand-blue-deep) 100%);
  }
  .back-visual {
    position: absolute;
    inset: 0;
    background:
      radial-gradient(ellipse at 70% 40%, rgba(80,150,220,0.45) 0%, rgba(20,90,170,0.15) 45%, rgba(0,0,0,0) 70%),
      linear-gradient(160deg, rgba(30,110,190,0.35), rgba(5,40,90,0.2));
  }
  .back-headline {
    position: absolute;
    left: 34px;
    top: 120px;
    color: var(--white);
  }
  .back-title {
    margin: 0;
    font-size: 28px;
    font-weight: 700;
    letter-spacing: 0.5px;
    line-height: 1.1;
  }
  .back-subtitle {
    margin: 4px 0 0;
    font-size: 15px;
    font-weight: 400;
  }
  .back-offer {
    position: absolute;
    left: 34px;
    bottom: 34px;
    color: var(--white);
  }
  .offer-line {
    margin: 0;
    font-size: 15px;
    font-weight: 400;
  }
  .offer-url {
    margin: 4px 0 0;
    font-size: 15px;
    font-weight: 400;
    letter-spacing: 0.3px;
  }
  .offer-url strong { font-weight: 700; }

  /* Front side */
  .card-front {
    left: 605px;
    top: 450px;
    background: linear-gradient(200deg, var(--paper) 40%, var(--paper-shade) 100%);
  }
  .front-band {
    position: absolute;
    inset: 0;
  }
  .brand {
    position: absolute;
    right: 30px;
    top: 34px;
    display: flex;
    align-items: center;
    gap: 10px;
  }
  .brand-dot {
    width: 16px;
    height: 16px;
    border-radius: 50%;
    background: var(--brand-blue);
  }
  .brand-name {
    font-size: 30px;
    font-weight: 800;
    color: var(--brand-blue);
    letter-spacing: 1px;
  }
  .brand-tag {
    position: absolute;
    right: 30px;
    top: 78px;
    font-size: 11px;
    font-weight: 600;
    color: var(--ink);
    letter-spacing: 1.5px;
    text-transform: uppercase;
  }
  .contact {
    position: absolute;
    right: 28px;
    top: 118px;
    margin: 0;
    padding: 0;
    list-style: none;
    text-align: right;
    color: var(--ink);
    font-size: 12.5px;
    line-height: 1.55;
  }
  .contact li {
    display: flex;
    justify-content: flex-end;
    align-items: center;
    gap: 7px;
  }
  .contact svg { width: 11px; height: 11px; flex: none; }
  .person {
    position: absolute;
    left: 110px;
    top: 160px;
  }
  .person-name {
    margin: 0;
    font-size: 19px;
    font-weight: 700;
    color: var(--brand-blue);
  }
  .person-role {
    margin: 0;
    font-size: 14px;
    color: var(--ink);
  }
</style>
</head>
<body>
<main class="canvas">

  <section class="card card-back" aria-label="Business card back">
    <div class="back-visual" role="img" aria-label="Photo of hands over a rising sales bar chart with figures, in blue tones"></div>
    <div class="back-headline">
      <h2 class="back-title">BOOST SALES</h2>
      <p class="back-subtitle">Using Rewards, Incentives &amp; Giveaways</p>
    </div>
    <div class="back-offer">
      <p class="offer-line">Get A Free Sample Package</p>
      <p class="offer-url">www.<strong>BrightlanePromotions</strong>.example</p>
    </div>
  </section>

  <section class="card card-front" aria-label="Business card front">
    <svg class="front-band" viewBox="0 0 525 300" preserveAspectRatio="none" aria-hidden="true">
      <polygon points="0,70 92,232 525,232 525,300 0,300" fill="#1474c0"/>
      <polygon points="0,70 92,232 0,300" fill="#0c5aa0" opacity="0.55"/>
    </svg>

    <div class="brand">
      <span class="brand-dot"></span>
      <span class="brand-name">LWP</span>
    </div>
    <div class="brand-tag">Brightlane Promotions</div>

    <ul class="contact">
      <li>1-555-302-4196
        <svg viewBox="0 0 12 12"><path d="M3 1 L5 3.5 L4 5 Q5.5 7.5 7 8 L8.5 7 L11 9 L9.5 11 Q4 10.5 1 2.5 Z" fill="#1474c0"/></svg>
      </li>
      <li>dorian@brightlanepromotions.example
        <svg viewBox="0 0 12 12"><rect x="0.5" y="2" width="11" height="8" fill="none" stroke="#1474c0" stroke-width="1.3"/><path d="M0.5 2 L6 7 L11.5 2" fill="none" stroke="#1474c0" stroke-width="1.3"/></svg>
      </li>
      <li>www.BrightlanePromotions.example
        <svg viewBox="0 0 12 12"><circle cx="6" cy="6" r="5.2" fill="none" stroke="#1474c0" stroke-width="1.2"/><path d="M1 6 H11 M6 1 Q3 6 6 11 Q9 6 6 1" fill="none" stroke="#1474c0" stroke-width="1"/></svg>
      </li>
    </ul>

    <div class="person">
      <h1 class="person-name">Dorian Pellow</h1>
      <p class="person-role">President, CEO</p>
    </div>
  </section>

</main>
</body>
</html>
```